creation of business cards for Velmora Sàrl

Velmora S% 26 # 224; rl is a soci% 26 # 233; t% 26 # 233; consultancy that accompanies companies in the development of their business on the market% 26 # 233; Switzerland by providing strategic contacts or market information; and by providing administrative or logistical support. Our consulting skills focus on sectors% 26 # 224; high value added% 26 # 233; e, such as trade in food goods% 26 # 39amp; drinks, fashion% 26amp; lifestyle, products and services for% 26 # 233; s in high-tech industries (pharmaceutical, chemical, m% 26 # 233; pricy 26% 23 #; cision) or sustainable solutions (% 26 # 233; energies renewable, mat% 26 # 233; recyclable materials). As part of the launch of our activity% 26 # 233;, we need% 26 # 39;% 26 # 233; to establish business cards to d% 26 # 233; work our new customers (Swiss or international).

Target Market(s)

Companies wishing to develop their activity% 26 # 233; s in Switzerland or% 26 # 224; l% 26 # 39;% 26 # 233; abroad (mainly in Europe).

Contact Information for Business Card

Prénom NOM
Velmora Sàrl
Bureau de Lavertin
Rue des Tilleuls 14, 2000 Neuchâtel
Tél. : 032 718 46 39
info@velmora-conseil.ch
www.velmora-conseil.ch

Font styles to use
Serif
Sans Serif

Colors

Designer to choose colors to be used in the design.

Requirements
Must have
• The logo The name of the company% 26 # 233; t% 26 # 233; (Velmora S% 26 # 224; rl) One field for the mailing address One field for the number% 26 # 233; ro de t% 26 # 233; l% 26 # 233; phone One field for the % 26 # 39; email address and website

```html
<!DOCTYPE html>
<html lang="fr">
<head>
<meta charset="utf-8">
<title>Velmora Sàrl – cartes de visite</title>
<link rel="stylesheet" href="https://fonts.googleapis.com/css2?family=Roboto:wght@300;400;700&display=swap">
<style>
  :root {
    --backdrop: #9e9ea0;
    --navy: #00405a;
    --mist: #a8b9c9;
    --paper: #ffffff;
  }
  * { margin: 0; padding: 0; box-sizing: border-box; }
  html, body {
    width: 1200px; height: 900px; overflow: hidden;
    background: var(--backdrop);
    font-family: "Roboto", Arial, sans-serif;
  }
  .canvas { position: relative; width: 1200px; height: 900px; }

  .card {
    position: absolute;
    left: 363px; width: 475px; height: 271px;
    overflow: hidden;
  }
  .card--front { top: 145px; background: var(--navy); }
  .card--back  { top: 484px; background: var(--paper); }

  .brand { position: absolute; display: flex; align-items: center; }
  .brand__square { display: block; border-radius: 5px; }
  .brand__name {
    font-weight: 300; text-transform: uppercase; line-height: 1;
    letter-spacing: 0.06em;
  }

  .card--front .brand { left: 83px; top: 112px; gap: 26px; }
  .card--front .brand__square { width: 47px; height: 47px; background: var(--paper); border-radius: 8px; }
  .card--front .brand__name { color: var(--paper); font-size: 41px; }

  .card--back .brand { left: 31px; top: 32px; gap: 15px; }
  .card--back .brand__square { width: 27px; height: 27px; background: var(--navy); }
  .card--back .brand__name { color: var(--navy); font-size: 25px; }

  .holder { position: absolute; left: 31px; top: 108px; }
  .holder__name { color: var(--navy); font-weight: 700; font-size: 20px; line-height: 24px; }
  .holder__company { color: var(--mist); font-weight: 300; font-size: 14px; line-height: 16px; }

  .contact { position: absolute; left: 31px; top: 156px; list-style: none; }
  .contact li {
    display: flex; align-items: center; gap: 5px;
    color: var(--navy); font-size: 13.5px; line-height: 16px; font-weight: 400;
  }
  .contact svg { width: 10px; height: 10px; fill: var(--mist); flex: none; }
  .contact .soft { color: var(--mist); }

  .address {
    position: absolute; left: 31px; top: 213px;
    color: var(--navy); font-size: 13.5px; line-height: 16px; font-style: normal;
  }
</style>
</head>
<body>
<main class="canvas">

  <section class="card card--front" aria-label="Recto">
    <div class="brand">
      <span class="brand__square"></span>
      <span class="brand__name">Velmora</span>
    </div>
  </section>

  <section class="card card--back" aria-label="Verso">
    <div class="brand">
      <span class="brand__square"></span>
      <span class="brand__name">Velmora</span>
    </div>

    <div class="holder">
      <p class="holder__name">Prénom NOM</p>
      <p class="holder__company">Velmora Sàrl</p>
    </div>

    <ul class="contact">
      <li>
        <svg viewBox="0 0 10 10" aria-hidden="true"><path d="M2 0.5 L3.6 2.8 L2.7 3.8 C3.3 5.2 4.6 6.6 6.1 7.3 L7.1 6.4 L9.5 8 L8.4 9.6 C4.5 9.3 0.7 5.5 0.4 1.6 Z"/></svg>
        Tél. : 032 718 46 39
      </li>
      <li>
        <svg viewBox="0 0 10 10" aria-hidden="true"><path d="M0 2 H10 V8.5 H0 Z M0.8 2.6 L5 5.8 L9.2 2.6" stroke="#fff" stroke-width="0.7"/></svg>
        info@velmora-conseil.ch
      </li>
      <li>
        <svg viewBox="0 0 10 10" aria-hidden="true"><circle cx="5" cy="5.5" r="4.5"/><path d="M0.5 5.5 H9.5 M5 1 V10" stroke="#fff" stroke-width="0.6"/></svg>
        <span>www.<span class="soft">velmora-conseil</span>.ch</span>
      </li>
    </ul>

    <address class="address">
      Bureau de Lavertin<br>
      Rue des Tilleuls 14, 2000 Neuchâtel
    </address>
  </section>

</main>
</body>
</html>
```